Pedicure Menu with 8 Scent Options

This design will be for a single page menu (front/back) that will display multiple different scent variations of a product. The purpose of this menu is to display to clients and show them the available options and benefits of each option.
The menu will be double sided.
The front page will include a header including brand logo and product name, and a total of 8 different scents including imagery and descriptive text.
The design should include the text provided for each scent. The design should have a layout that is structured/organized, easy to read, and has bright imagery that represents each scent.
An example is a modular layout using boxes that highlight a different scent within each box. Lavender scent should include aesthetic images of lavender flower and/or the color purple.
The back page will include brand logo, overall product description, and additional brief text that explains each step of the product.
The final size of the design should be 8.5"x11", produced in InDesign format, with all layers editable for future changes.
NOTE: Please carefully review the attached design brief that includes additional information, and all necessary text to include in the design.
Target Market(s)
Beauty/Spa Clients
Industry/Entity Type
Beauty
Requirements
Must have
- Bright and Vivid Imagery/Illustrations
Nice to have
- Background design that utilizes, lines, shapes, or other elements.

```html
<!DOCTYPE html>
<html lang="en">
<head>
<meta charset="utf-8">
<title>Velora Deluxe Pedicure 4-Step Menu</title>
<link rel="stylesheet" href="https://fonts.googleapis.com/css2?family=Montserrat:wght@500;600;700&family=Fira+Sans:wght@400;500;700&display=swap">
<style>
:root{
  --backdrop:#cfcfcd;
  --paper:#ffffff;
  --ink:#111111;
  --band:#000000;
  --lav:#957bb6; --lav-bg:#f1eff4;
  --man:#f07022; --man-bg:#fdf0dc;
  --cuc:#6bb33f; --cuc-bg:#eaf2e4;
  --jas:#b1d44a; --jas-bg:#f2f7e4;
  --rose:#d71f27; --rose-bg:#fbe5e7;
  --mint:#1cb892; --mint-bg:#e2f5f1;
  --honey:#f2a22a; --honey-bg:#fdf0dc;
  --tea:#2f6a2f; --tea-bg:#dde4dc;
  --step1:#d8e8a6; --step2:#b4d9a0; --step3:#f8d394; --step4:#8fdcc4;
  --leaf:#8aa55a;
}
*{box-sizing:border-box;margin:0;padding:0}
html,body{width:1200px;height:1200px;overflow:hidden}
body{background:var(--backdrop);position:relative;font-family:"Fira Sans",sans-serif;color:var(--ink)}
.page{position:absolute;top:244px;width:553px;height:711px;background:var(--paper);overflow:hidden}
.page--front{left:32px}
.page--back{left:616px}
.page__band{position:absolute;left:0;right:0;bottom:0;height:16px;background:var(--band)}
.corner-art{position:absolute;top:0;width:120px;height:130px;background:linear-gradient(160deg,rgba(138,165,90,.45),rgba(230,230,225,.3) 70%,transparent);border-radius:0 0 60px 0}
.corner-art--left{left:0}
.corner-art--right{right:0;transform:scaleX(-1)}
.brand{position:absolute;top:22px;left:0;right:0;display:flex;justify-content:center;align-items:center;gap:10px}
.brand__dot{width:12px;height:12px;border-radius:50%;background:var(--ink)}
.brand__name{font-family:"Montserrat",sans-serif;font-weight:500;font-size:50px;letter-spacing:2px;line-height:1}
.title{position:absolute;top:105px;left:0;right:0;text-align:center;font-family:"Montserrat",sans-serif;font-weight:700;font-size:27px}
.pill{position:absolute;top:145px;left:179px;width:198px;height:25px;border-radius:13px;background:var(--ink);color:#fff;font-family:"Montserrat",sans-serif;font-weight:600;font-size:17px;text-align:center;line-height:25px}
.scent{position:absolute;width:254px;height:115px;border-radius:14px 14px 14px 14px;overflow:hidden;background:var(--bg)}
.scent__head{height:27px;background:var(--c);color:#fff;font-family:"Montserrat",sans-serif;font-weight:700;font-size:14px;text-align:center;line-height:28px}
.scent__img{position:absolute;left:10px;top:36px;width:56px;height:72px;border-radius:8px}
.scent__text{position:absolute;left:76px;right:6px;top:33px;font-size:7.6px;line-height:12.3px;text-align:justify}
.col-a{left:17px;border-radius:14px 14px 14px 0}
.col-b{left:284px;border-radius:14px 14px 0 14px}
.intro{position:absolute;top:175px;left:60px;right:60px;text-align:center;font-size:13.6px;line-height:19.6px}
.tagline{position:absolute;top:244px;left:0;right:0;text-align:center;font-weight:700;font-size:16.5px}
.scene-art{position:absolute;border-radius:10px}
.steps{position:absolute;top:343px;left:0;width:553px;height:352px;display:grid;grid-template-columns:1fr 1fr;grid-template-rows:176px 176px}
.step{position:relative;text-align:center;background:var(--c)}
.step__photo{position:absolute;top:17px;left:50%;transform:translateX(-50%);width:114px;height:90px;border:2px solid #222;border-radius:24px 8px 24px 8px;background:var(--p)}
.step__name{position:absolute;top:122px;left:0;right:0;font-family:"Montserrat",sans-serif;font-weight:600;font-size:16px}
.step__desc{position:absolute;top:147px;left:0;right:0;font-size:13.4px}
</style>
</head>
<body>

<section class="page page--front">
  <div class="corner-art corner-art--left" role="img" aria-label="Bamboo stalks and leaves decoration"></div>
  <div class="corner-art corner-art--right" role="img" aria-label="Bamboo stalks and leaves decoration"></div>
  <div class="brand"><span class="brand__dot"></span><span class="brand__name">Velora</span></div>
  <h1 class="title">Deluxe Pedicure 4-Step</h1>
  <div class="pill">Pick Your Pedicure</div>

  <article class="scent col-a" style="top:191px;--c:var(--lav);--bg:var(--lav-bg)">
    <h2 class="scent__head">Lavender</h2>
    <div class="scent__img" role="img" aria-label="Bunch of lavender flowers" style="background:linear-gradient(160deg,#8a6fc4,#c5b3e3)"></div>
    <p class="scent__text">Melt away the stresses of the day with a delicate, sweet smell that is floral and woodsy at the same time. Lavender is a calming scent for relaxation that puts us in a better mood and helps create a sense of tranquility and peacefulness</p>
  </article>
  <article class="scent col-b" style="top:191px;--c:var(--man);--bg:var(--man-bg)">
    <h2 class="scent__head">Mandarin</h2>
    <div class="scent__img" role="img" aria-label="Fresh mandarin oranges, whole and sliced" style="background:linear-gradient(160deg,#f5a035,#f06a1a)"></div>
    <p class="scent__text">Uplift your senses with a fruity and sweet aroma that promotes clarity, radiance and a smooth, even skin tone. A citrus blend of essential oils works great to polish dull skin, reduce wrinkles, and correct spots</p>
  </article>

  <article class="scent col-a" style="top:320px;--c:var(--cuc);--bg:var(--cuc-bg)">
    <h2 class="scent__head">Cucumber-Melon</h2>
    <div class="scent__img" role="img" aria-label="Cantaloupe slice and cucumbers" style="background:linear-gradient(160deg,#f3a64a,#6aa63a)"></div>
    <p class="scent__text">Jump into a refreshing blend of crisp cucumber, watery honeydew, and summer cantaloupe. Perfect for capturing the essence of a summer day. Bamboo and aloe extract help cool your skin after a day in the sun</p>
  </article>
  <article class="scent col-b" style="top:320px;--c:var(--jas);--bg:var(--jas-bg)">
    <h2 class="scent__head">Jasmine</h2>
    <div class="scent__img" role="img" aria-label="White jasmine flowers with leaves" style="background:linear-gradient(160deg,#ffffff,#9cc264)"></div>
    <p class="scent__text">Embrace the warmth of a rich and sensual floral scent that boosts your energy levels and helps make your day better and brighter. A symbol of purity, love, and beauty – Jasmine helps to reduce exhaustion, nervousness, and stress</p>
  </article>

  <article class="scent col-a" style="top:448px;--c:var(--rose);--bg:var(--rose-bg)">
    <h2 class="scent__head">Rose</h2>
    <div class="scent__img" role="img" aria-label="Cluster of red roses" style="background:linear-gradient(160deg,#d3202a,#8e0f16)"></div>
    <p class="scent__text">Fall in love with a delicate floral twist of spicy and sweet that nourishes your skin and calms the mind. Essential oils help to reduce fine lines and protect the skin from UV damage</p>
  </article>
  <article class="scent col-b" style="top:448px;--c:var(--mint);--bg:var(--mint-bg)">
    <h2 class="scent__head">Mint</h2>
    <div class="scent__img" role="img" aria-label="Fresh mint sprigs" style="background:linear-gradient(160deg,#4a9a4a,#2c6b2f)"></div>
    <p class="scent__text">Rejuvenate your body with a cool mix of peppermint and spearmint that prevents skin damage, alleviates inflamed skin, and acts as a splash of tonic for the senses. Infused with eucalyptus to leave you clean, cool, and crisp</p>
  </article>

  <article class="scent col-a" style="top:576px;--c:var(--honey);--bg:var(--honey-bg)">
    <h2 class="scent__head">Milk &amp; Honey</h2>
    <div class="scent__img" role="img" aria-label="Honey jar with dipper and glass of milk" style="background:linear-gradient(160deg,#f6f3ea,#e48a18)"></div>
    <p class="scent__text">Discover one of nature's most luxurious skin cleansers and softeners. Creamy milk is full of rich essential vitamins that supply abundant moisture and improves skin elasticity. Sweet honey contains antioxidants and other nutrients that slow down skin aging</p>
  </article>
  <article class="scent col-b" style="top:576px;--c:var(--tea);--bg:var(--tea-bg)">
    <h2 class="scent__head">Green-Tea</h2>
    <div class="scent__img" role="img" aria-label="Fresh green tea leaves over dried tea" style="background:linear-gradient(160deg,#5f9a3a,#3a3328)"></div>
    <p class="scent__text">Restore a sense of serenity with fragrant green tea extract that helps to relax the mind, reduces redness and swelling, and leaves the skin feeling hydrated, silky, and smooth. A natural detoxification that will supplies abundant moisture to the skin</p>
  </article>
  <div class="page__band"></div>
</section>

<section class="page page--back">
  <div class="corner-art corner-art--left" role="img" aria-label="Bamboo stalks and leaves decoration"></div>
  <div class="corner-art corner-art--right" role="img" aria-label="Bamboo stalks and leaves decoration"></div>
  <div class="brand"><span class="brand__dot"></span><span class="brand__name">Velora</span></div>
  <h1 class="title">Deluxe Pedicure 4-Step</h1>
  <p class="intro">Velora Deluxe Pedicure 4-Step will transform your pedicure experience and immerse your senses into a floral paradise designed to rejuvenate your body.</p>
  <p class="tagline">Sit back, relax, and enjoy.</p>
  <div class="scene-art" role="img" aria-label="Lit spa candles" style="left:0;top:230px;width:90px;height:113px;background:linear-gradient(180deg,#f4c9a0,#e6e4df)"></div>
  <div class="scene-art" role="img" aria-label="Stack of spa stones" style="left:243px;top:290px;width:66px;height:53px;background:linear-gradient(180deg,#8c8c8c,#5a5a5a);border-radius:30px"></div>
  <div class="scene-art" role="img" aria-label="Green leafy branch" style="left:463px;top:270px;width:90px;height:73px;background:linear-gradient(160deg,#9bb56e,rgba(255,255,255,0))"></div>

  <div class="steps">
    <div class="step" style="--c:var(--step1)">
      <div class="step__photo" role="img" aria-label="Spoon of bath salt over a foot soak" style="--p:linear-gradient(160deg,#d9c6b4,#f3ece6)"></div>
      <h3 class="step__name">1. Salt Soak</h3>
      <p class="step__desc">Detoxifies and deodorizes your feet.</p>
    </div>
    <div class="step" style="--c:var(--step2)">
      <div class="step__photo" role="img" aria-label="Feet with sugar scrub over a basin" style="--p:linear-gradient(160deg,#8fb06a,#e9c9b0)"></div>
      <h3 class="step__name">2. Sugar Scrub</h3>
      <p class="step__desc">Gently exfoliates dead skin.</p>
    </div>
    <div class="step" style="--c:var(--step3)">
      <div class="step__photo" role="img" aria-label="Clay masque applied to a foot" style="--p:linear-gradient(160deg,#f2ded2,#8a6a4e)"></div>
      <h3 class="step__name">3. Foot Masque</h3>
      <p class="step__desc">Cleanses pores for smoother skin.</p>
    </div>
    <div class="step" style="--c:var(--step4)">
      <div class="step__photo" role="img" aria-label="Lotion massaged onto a foot" style="--p:linear-gradient(160deg,#e8c1a6,#f4ddcf)"></div>
      <h3 class="step__name">4. Massage Lotion</h3>
      <p class="step__desc">Hydrates and soothes skin.</p>
    </div>
  </div>
  <div class="page__band"></div>
</section>

</body>
</html>
```